Construction Company Business Card

Business Card Design using new Logo

Contact Information for Business Card

include all company info and website

Requirements
Must have
• Marlon Ridgeway - President
ph. 254-716-5093
Cedar Hollow, TX
marlon@stonefieldworks.com
www.stonefieldworks.com

```html
<!DOCTYPE html>
<html lang="en">
<head>
<meta charset="utf-8">
<title>Stonefield Works – Business Card</title>
<link href="https://fonts.googleapis.com/css2?family=Lato:wght@400;700;900&display=swap" rel="stylesheet">
<style>
  :root {
    --stage: #8e8e8e;
    --card: #000000;
    --red: #c8202a;
    --red-deep: #8f141b;
    --silver: #cfcfd3;
  }
  html, body {
    margin: 0;
    width: 1200px;
    height: 1200px;
    overflow: hidden;
    background: var(--stage);
    font-family: "Lato", sans-serif;
  }
  .card {
    position: absolute;
    left: 171px;
    width: 847px;
    height: 484px;
    background: var(--card);
    border-radius: 19px;
    overflow: hidden;
  }
  .card--front { top: 94px; }
  .card--back { top: 612px; }

  .front-band {
    position: absolute;
    left: 0; right: 0; bottom: 0;
    height: 124px;
    background: linear-gradient(180deg, #000 0%, var(--red-deep) 35%, var(--red) 100%);
  }
  .contact-name {
    position: absolute;
    left: 29px; top: 68px;
    margin: 0;
    color: var(--red);
    font-weight: 700;
    font-size: 31px;
    line-height: 1;
  }
  .contact-title {
    position: absolute;
    left: 29px; top: 104px;
    margin: 0;
    color: var(--silver);
    font-weight: 700;
    font-size: 22px;
    line-height: 1;
    letter-spacing: 0.5px;
  }
  .title-rule {
    position: absolute;
    left: 30px; top: 151px;
    width: 106px; height: 3px;
    background: var(--red);
  }
  .contact-list {
    position: absolute;
    left: 29px; top: 182px;
    margin: 0; padding: 0;
    list-style: none;
  }
  .contact-list li {
    display: flex;
    align-items: center;
    height: 34px;
    color: var(--red);
    font-weight: 700;
    font-size: 22px;
    letter-spacing: 0.4px;
  }
  .contact-list li:first-child { font-size: 23px; letter-spacing: 1px; }
  .contact-icon {
    width: 21px; height: 21px;
    margin-right: 9px;
    flex: none;
  }
  .brand-name {
    position: absolute;
    margin: 0;
    color: var(--silver);
    font-weight: 700;
    letter-spacing: 2px;
    white-space: nowrap;
    display: flex;
    align-items: center;
  }
  .brand-mark {
    display: inline-block;
    background: var(--red);
    border-radius: 50%;
    flex: none;
  }
  .card--front .brand-name {
    right: 30px; top: 148px;
    font-size: 34px;
  }
  .card--front .brand-mark { width: 16px; height: 16px; margin-right: 12px; }
  .location {
    position: absolute;
    right: 30px; top: 326px;
    margin: 0;
    color: var(--red);
    font-weight: 700;
    font-size: 23px;
    letter-spacing: 0.5px;
  }
  .card--back .brand-name {
    left: 0; right: 0; top: 160px;
    justify-content: center;
    font-size: 53px;
    letter-spacing: 3px;
  }
  .card--back .brand-mark { width: 25px; height: 25px; margin-right: 20px; }
  .back-web {
    position: absolute;
    left: 0; right: 0; top: 418px;
    display: flex;
    align-items: center;
    justify-content: center;
    gap: 10px;
  }
  .back-web span {
    color: var(--silver);
    font-weight: 700;
    font-size: 29.5px;
    letter-spacing: 0.5px;
  }
  .web-rule {
    height: 3px;
    width: 200px;
  }
  .web-rule--left { background: linear-gradient(90deg, transparent, var(--red) 40%); }
  .web-rule--right { background: linear-gradient(90deg, var(--red) 60%, transparent); }
</style>
</head>
<body>

<section class="card card--front">
  <div class="front-band" role="img" aria-label="Decorative red and silver wave band"></div>

  <h1 class="contact-name">Marlon Ridgeway</h1>
  <p class="contact-title">President</p>
  <div class="title-rule"></div>

  <ul class="contact-list">
    <li>
      <svg class="contact-icon" viewBox="0 0 24 24" aria-hidden="true">
        <path fill="var(--silver)" d="M6.6 10.8c1.4 2.8 3.8 5.1 6.6 6.6l2.2-2.2c.3-.3.7-.4 1-.2 1.1.4 2.3.6 3.6.6.6 0 1 .4 1 1V20c0 .6-.4 1-1 1C10.6 21 3 13.4 3 4c0-.6.4-1 1-1h3.5c.6 0 1 .4 1 1 0 1.3.2 2.5.6 3.6.1.3 0 .7-.2 1z"/>
      </svg>
      254-716-5093
    </li>
    <li>
      <svg class="contact-icon" viewBox="0 0 24 24" aria-hidden="true">
        <rect x="2" y="5" width="20" height="14" fill="var(--silver)"/>
        <path d="M2 5l10 8 10-8M2 19l7-7M22 19l-7-7" fill="none" stroke="#000" stroke-width="1.5"/>
      </svg>
      marlon@stonefieldworks.com
    </li>
    <li>
      <svg class="contact-icon" viewBox="0 0 24 24" aria-hidden="true">
        <circle cx="12" cy="12" r="10" fill="var(--silver)"/>
        <path d="M2 12h20M12 2c3 3 3 17 0 20M12 2c-3 3-3 17 0 20" fill="none" stroke="#000" stroke-width="1.2"/>
      </svg>
      www.stonefieldworks.com
    </li>
  </ul>

  <p class="brand-name"><span class="brand-mark"></span>STONEFIELD WORKS</p>
  <p class="location">Cedar Hollow, TX</p>
</section>

<section class="card card--back">
  <p class="brand-name"><span class="brand-mark"></span>STONEFIELD WORKS</p>
  <div class="back-web">
    <div class="web-rule web-rule--left"></div>
    <span>www.stonefieldworks.com</span>
    <div class="web-rule web-rule--right"></div>
  </div>
</section>

</body>
</html>
```